"Built on the grind" fitness and nutrition website/blog/forum

We need a website design for a gym training/nutrition website/blog. It is going to eventually have articles aimed at both men and women and will have content about exercise, nutrition, and the science behind both.

I want to have:
a home page
a page for all articles/blog posts about Nutrition
a page for all articles/blog posts about Training
a page where we can share articles about workouts targeting different muscle groups
a forum, where people can discuss nutrition and training (I would want this to be fairly simple to use and control as I am not a coder/programmer)

Design wise, I would like to use high contrast colours, such as black and white, but definitely open to some sort of colour theme, maybe some blue, or red, or purple, I am not sure, I would have to see an example.

We will be monetising this site with adverts, so there needs to be some space built in for this in the theme, however we don't want this to be overbearing, I don't want this to look like a spam site.

We have a logo, I have attached this. I haven't written any content for the homepage yet, as I wanted the design first before I worked out what to write and where to put it.

We will have social media accounts on instagram, twitter and facebook so would like buttons on the header and footer for these.

Target Market(s)

Fitness enthusiasts

Industry/Entity Type

fitness

Coding

Coded - Design and coding required

Number of Pages Required

5+ page

Font styles to use
Serif
Sans Serif

Colors

Designer to choose colors to be used in the design.

Requirements
Must have
• Space for some ads, a forum area, a page for nutrition blog posts, a page for training posts, a page for workout posts.

```html
<!DOCTYPE html>
<html lang="en">
<head>
<meta charset="utf-8">
<title>Built on the grind</title>
<link rel="stylesheet" href="https://fonts.googleapis.com/css2?family=Outfit:wght@400;500;600&display=swap">
<style>
:root{
  --bg:#ffffff;
  --band:#e4e6eb;
  --panel:#eeeff2;
  --card:#f2f2f4;
  --ink:#1c1c22;
  --muted:#55565c;
  --red:#e8202a;
  --blue:#1d5a9e;
  --black:#0b0b0c;
}
*{margin:0;padding:0;box-sizing:border-box}
html,body{width:1200px;height:3178px;overflow:hidden;background:var(--bg)}
body{font-family:"Outfit",sans-serif;color:var(--ink);position:relative}
.page{position:absolute;left:1px;top:29px;width:724px;height:1885px;transform:scale(1.655);transform-origin:0 0}
.page *{position:absolute}
.page svg *{position:static}
.band{left:0;top:0;width:724px;height:170px;background:var(--band)}
.brand{font-weight:600;font-size:13px;color:var(--ink);white-space:nowrap;display:flex;align-items:center;gap:5px}
.brand i{position:static;display:block;width:9px;height:9px;background:var(--red)}
.social-label{font-size:6.5px;font-weight:600;color:var(--blue);letter-spacing:.3px}
.dot{width:11px;height:11px;border-radius:50%;background:#444a55}
.login{left:563px;top:25px;width:68px;height:20px;background:var(--red);color:#fff;font-size:7px;font-weight:500;display:flex;align-items:center;justify-content:center;letter-spacing:.4px}
.nav{font-size:7px;font-weight:500;letter-spacing:.3px;white-space:nowrap}
.nav.active{color:var(--red)}
.hero-panel{left:46px;top:94px;width:217px;height:243px;background:var(--black)}
.hero-photo{left:263px;top:94px;width:415px;height:243px;background:linear-gradient(120deg,#3b3b40 0%,#6d6a68 35%,#b9b3ad 55%,#4a4848 80%,#2a2a2d 100%)}
.hero-photo::before{content:"";position:absolute;left:0;top:0;width:100%;height:40px;background:linear-gradient(90deg,#c75a1f,#e07a2c 60%,#a84a18)}
.w{color:#fff}
.kicker{font-size:7px;color:var(--red);letter-spacing:.3px}
.btn-line{border:1px solid var(--red);color:var(--red);font-size:6.5px;font-weight:500;display:flex;align-items:center;justify-content:center;letter-spacing:.4px;background:transparent}
.btn-fill{background:var(--red);color:#fff;font-size:6.5px;font-weight:500;display:flex;align-items:center;justify-content:center;letter-spacing:.4px}
.sec-title{font-size:17px;font-weight:500;color:var(--blue);letter-spacing:.5px}
.rule{height:1px;background:var(--blue)}
.img{display:block}
.tag{background:var(--blue);color:#fff;font-size:6px;font-weight:500;padding:0 5px;height:10px;line-height:10px;letter-spacing:.3px}
.card-body{background:var(--card)}
.date{font-size:7px;color:var(--blue);text-align:center;width:100%}
.post-title{font-size:9.5px;line-height:13px;text-align:center}
.post-text{font-size:6.3px;line-height:10.5px;text-align:center;color:var(--muted)}
.side{background:var(--panel)}
.side-h{font-size:10px;font-weight:500;color:var(--blue);letter-spacing:.3px}
.side-u{width:23px;height:1px;background:var(--blue)}
.side-item{font-size:7px}
.side-div{height:1px;background:#d2d4da}
.chip{height:14px;border:1px solid #c9cbd1;font-size:6px;color:var(--muted);display:flex;align-items:center;justify-content:center;background:#f7f7f9}
.chip.on{background:var(--blue);color:#fff;border-color:var(--blue)}
.small{font-size:6.5px;line-height:9.5px;color:var(--muted)}
.input{border:1px solid #c9cbd1;background:#fff;font-size:6px;color:var(--muted);padding-left:7px;display:flex;align-items:center}
.forum-title{font-size:8px;font-weight:600}
.meta{font-size:6.5px;color:var(--blue);letter-spacing:.3px}
.foot-nav{font-size:6.8px;color:var(--muted)}
</style>
</head>
<body>
<main class="page">
  <!-- Header -->
  <div class="band"></div>
  <div class="brand" style="left:70px;top:42px"><i></i>Built on the grind</div>
  <div class="social-label" style="left:441px;top:32px">GET SOCIAL!</div>
  <div class="dot" style="left:493px;top:29px"></div>
  <div class="dot" style="left:510px;top:29px"></div>
  <div class="dot" style="left:527px;top:29px"></div>
  <div class="login">
    <svg width="7" height="7" viewBox="0 0 10 10" style="margin-right:4px"><circle cx="5" cy="3" r="2.3" fill="#fff"/><path d="M1 10 C1 6 9 6 9 10Z" fill="#fff"/></svg>LOGIN
  </div>
  <div class="nav active" style="left:239px;top:68px">HOME</div>
  <div class="nav" style="left:284px;top:68px">ABOUT US</div>
  <div class="nav" style="left:345px;top:68px">NUTRITION</div>
  <div class="nav" style="left:409px;top:68px">TRAINING</div>
  <div class="nav" style="left:468px;top:68px">WORKOUTS</div>
  <div class="nav" style="left:535px;top:68px">FORUM</div>
  <div class="nav" style="left:584px;top:68px">CONTACT US</div>

  <!-- Hero -->
  <section class="hero-panel"></section>
  <div class="hero-photo img" role="img" aria-label="Woman resting on a gym bench drinking from a bottle, dumbbell racks behind"></div>
  <div class="kicker" style="left:78px;top:123px">– NUTRITION</div>
  <h1 class="w" style="left:78px;top:144px;width:170px;font-size:10.5px;line-height:13px;font-weight:500">Contrary to Popular Belief, lorem Ipsum is Site</h1>
  <p class="w" style="left:78px;top:182px;width:170px;font-size:7px;line-height:10.5px">There are many variations of passages of Lorem Ipsum available, but the majority have suffered...</p>
  <div class="btn-line" style="left:78px;top:232px;width:68px;height:19px">READ MORE</div>
  <div class="w" style="left:78px;top:302px;font-size:7px">← PREV</div>
  <div class="w" style="left:148px;top:302px;font-size:7px">3/2</div>
  <div style="left:205px;top:302px;font-size:7px;color:var(--red)">NEXT →</div>

  <!-- Featured Blog -->
  <div class="rule" style="left:138px;top:384px;width:47px"></div>
  <h2 class="sec-title" style="left:209px;top:372px">Featured Blog</h2>
  <div class="rule" style="left:356px;top:384px;width:46px"></div>

  <div class="img" role="img" aria-label="Plate of salad with egg, tomatoes and avocado on a wooden table" style="left:46px;top:425px;width:448px;height:169px;background:linear-gradient(100deg,#6b5a48 0%,#8a7560 30%,#4d7a9a 45%,#7fa25a 60%,#c76a3a 75%,#8a7158 100%)"></div>
  <div class="tag" style="left:48px;top:427px">NUTRITION</div>
  <article class="card-body" style="left:170px;top:558px;width:200px;height:139px">
    <div class="date" style="top:24px">▣ DEC 18ᵀᴴ 2022</div>
    <div class="post-title" style="left:14px;top:37px;width:172px">Contrary to popular belief, Lorem Ipsum is not simply</div>
    <div class="post-text" style="left:10px;top:84px;width:180px">There are many variations of passages of Lorem Ipsum available, but the majority have care suffered alteration in some form...</div>
  </article>
  <div class="btn-fill" style="left:243px;top:685px;width:57px;height:15px">READ MORE</div>

  <!-- Card grid -->
  <div class="img" role="img" aria-label="Group doing sit-ups on gym floor" style="left:46px;top:720px;width:216px;height:124px;background:linear-gradient(120deg,#3a2f2a,#b27a55 50%,#2f2b2a)"></div>
  <div class="tag" style="left:48px;top:722px">TRAINING</div>
  <article class="card-body" style="left:46px;top:844px;width:216px;height:127px">
    <div class="date" style="top:14px">▣ SEP 20ᵀᴴ 2022</div>
    <div class="post-title" style="left:20px;top:28px;width:176px">Contrary to popular belief, Lorem Ipsum is not simply</div>
    <div class="post-text" style="left:20px;top:71px;width:176px">There are many variations of passages of Lorem Ipsum available, but the majority have care suffered alteration in some form...</div>
  </article>
  <div class="btn-line" style="left:125px;top:961px;width:59px;height:14px;background:#fff">READ MORE</div>

  <div class="img" role="img" aria-label="Man and woman doing push-ups on kettlebells" style="left:277px;top:720px;width:217px;height:124px;background:linear-gradient(120deg,#5c6068,#a9a8a6 50%,#3c3e44)"></div>
  <div class="tag" style="left:279px;top:722px">WORKOUTS</div>
  <article class="card-body" style="left:277px;top:844px;width:217px;height:127px">
    <div class="date" style="top:14px">▣ DEC 18ᵀᴴ 2022</div>
    <div class="post-title" style="left:20px;top:28px;width:177px">Contrary to popular belief, Lorem Ipsum is not simply</div>
    <div class="post-text" style="left:20px;top:71px;width:177px">There are many variations of passages of Lorem Ipsum available, but the majority have care suffered alteration in some form...</div>
  </article>
  <div class="btn-line" style="left:357px;top:961px;width:59px;height:14px;background:#fff">READ MORE</div>

  <div class="img" role="img" aria-label="Man lifting a barbell in a gym" style="left:46px;top:995px;width:216px;height:124px;background:linear-gradient(120deg,#2d2c2d,#7a726b 50%,#1f1f21)"></div>
  <div class="tag" style="left:48px;top:997px">WORKOUTS</div>
  <article class="card-body" style="left:46px;top:1119px;width:216px;height:127px">
    <div class="date" style="top:14px">▣ DEC 18ᵀᴴ 2022</div>
    <div class="post-title" style="left:20px;top:28px;width:176px">Contrary to popular belief, Lorem Ipsum is not simply</div>
    <div class="post-text" style="left:20px;top:71px;width:176px">There are many variations of passages of Lorem Ipsum available, but the majority have care suffered alteration in some form...</div>
  </article>
  <div class="btn-line" style="left:125px;top:1236px;width:59px;height:14px;background:#fff">READ MORE</div>

  <div class="img" role="img" aria-label="Woman training with a cable machine" style="left:277px;top:995px;width:217px;height:124px;background:linear-gradient(120deg,#4a4644,#b49a86 50%,#3a3633)"></div>
  <div class="tag" style="left:279px;top:997px">TRAINING</div>
  <article class="card-body" style="left:277px;top:1119px;width:217px;height:127px">
    <div class="date" style="top:14px">▣ SEP 20ᵀᴴ 2022</div>
    <div class="post-title" style="left:20px;top:28px;width:177px">Contrary to popular belief, Lorem Ipsum is not simply</div>
    <div class="post-text" style="left:20px;top:71px;width:177px">There are many variations of passages of Lorem Ipsum available, but the majority have care suffered alteration in some form...</div>
  </article>
  <div class="btn-line" style="left:357px;top:1236px;width:59px;height:14px;background:#fff">READ MORE</div>

  <div class="btn-fill" style="left:231px;top:1275px;width:78px;height:20px">VIEW ALL BLOG</div>

  <!-- Sidebar -->
  <aside class="side" style="left:508px;top:376px;width:170px;height:452px"></aside>
  <div class="side-h" style="left:522px;top:389px">Blog Category</div>
  <div class="side-u" style="left:522px;top:408px"></div>
  <div class="side-item" style="left:522px;top:422px">Nutrition</div>
  <div class="side-item" style="left:522px;top:440px;color:var(--red)">--- Training</div>
  <div class="side-item" style="left:522px;top:457px">Workouts</div>
  <div class="side-item" style="left:522px;top:474px">Forum</div>
  <div class="side-div" style="left:522px;top:503px;width:142px"></div>
  <div class="side-h" style="left:522px;top:516px">About Us</div>
  <div class="side-u" style="left:522px;top:535px"></div>
  <div class="img" role="img" aria-label="Woman stretching on a gym floor" style="left:522px;top:550px;width:142px;height:97px;background:linear-gradient(120deg,#8a6a50,#d6c1ab 50%,#5b4a3e)"></div>
  <p class="small" style="left:522px;top:660px;width:142px;color:var(--ink)">Contrary to popular belief, Lorem Ipsum is not simply random text. It has roots in a piece of just classical Latin literature...</p>
  <div class="btn-line" style="left:522px;top:720px;width:69px;height:19px;background:#fff">READ MORE</div>
  <div class="side-div" style="left:522px;top:755px;width:142px"></div>
  <div class="side-h" style="left:522px;top:767px">Get Social</div>
  <div class="side-u" style="left:522px;top:786px"></div>
  <div class="dot" style="left:523px;top:800px;width:13px;height:13px"></div>
  <div class="dot" style="left:544px;top:800px;width:13px;height:13px"></div>
  <div class="dot" style="left:566px;top:800px;width:13px;height:13px"></div>
  <div class="dot" style="left:587px;top:800px;width:13px;height:13px"></div>

  <div class="img" role="img" aria-label="Advertisement banner" style="left:508px;top:843px;width:170px;height:149px;background:linear-gradient(160deg,#0f4a5c,#0a2d3c 70%,#071f2a)"></div>

  <aside class="side" style="left:508px;top:1007px;width:170px;height:289px"></aside>
  <div class="side-h" style="left:522px;top:1019px">Tag</div>
  <div class="side-u" style="left:522px;top:1038px"></div>
  <div class="chip" style="left:522px;top:1055px;width:44px">Nutrition</div>
  <div class="chip" style="left:570px;top:1055px;width:40px">Exercise</div>
  <div class="chip" style="left:615px;top:1055px;width:32px">Fitness</div>
  <div class="chip" style="left:522px;top:1075px;width:28px">Diet</div>
  <div class="chip on" style="left:553px;top:1075px;width:64px">Health &amp; Beauty</div>
  <div class="chip" style="left:620px;top:1075px;width:29px">Food</div>
  <div class="chip" style="left:522px;top:1096px;width:41px">Training</div>
  <div class="chip" style="left:572px;top:1096px;width:37px">Workouts</div>
  <div class="chip" style="left:614px;top:1096px;width:36px">Exercise</div>
  <div class="chip" style="left:522px;top:1116px;width:38px">Fitness</div>
  <div class="chip" style="left:564px;top:1116px;width:31px">Food</div>
  <div class="chip" style="left:599px;top:1116px;width:35px">Lifestyle</div>
  <div class="side-h" style="left:522px;top:1160px">Subscribes</div>
  <div class="side-u" style="left:522px;top:1179px"></div>
  <p class="small" style="left:522px;top:1192px;width:142px;color:var(--ink)">Subscribe to my newsletter to get latest scoop right to your inbox.</p>
  <div class="input" style="left:522px;top:1224px;width:142px;height:19px">Your email ...</div>
  <div class="btn-line" style="left:522px;top:1252px;width:59px;height:19px;background:#fff">SUBSCRIBE</div>

  <!-- Forum -->
  <section class="side" style="left:46px;top:1336px;width:632px;height:213px"></section>
  <div class="img" role="img" aria-label="Forum member avatar" style="left:92px;top:1368px;width:48px;height:48px;border-radius:50%;background:linear-gradient(135deg,#4a5a6e,#a89282)"></div>
  <div class="forum-title" style="left:153px;top:1368px">Contrary to popular belief</div>
  <div class="small" style="left:153px;top:1380px;font-size:6px">4 Hours ago</div>
  <p class="small" style="left:153px;top:1400px;width:190px;color:var(--ink)">Lorem Ipsum is simply dummy text of the printing and typesetting industry. Lorem Ipsum has been the industry's standard dummy text ever since the 1500s, when an unknown printer took ...</p>
  <div class="meta" style="left:153px;top:1456px">▲ J. MARLOW &nbsp;&nbsp;&nbsp;&nbsp; ▪ 10</div>

  <div class="img" role="img" aria-label="Forum member avatar" style="left:370px;top:1368px;width:48px;height:48px;border-radius:50%;background:linear-gradient(135deg,#3c3532,#9a7c66)"></div>
  <div class="forum-title" style="left:431px;top:1368px">Contrary to popular belief</div>
  <div class="small" style="left:431px;top:1380px;font-size:6px">4 Hours ago</div>
  <p class="small" style="left:431px;top:1400px;width:190px;color:var(--ink)">Lorem Ipsum is simply dummy text of the printing and typesetting industry. Lorem Ipsum has been the industry's standard dummy text ever since the 1500s, when an unknown printer took ...</p>
  <div class="meta" style="left:431px;top:1456px">▲ J. MARLOW &nbsp;&nbsp;&nbsp;&nbsp; ▪ 10</div>
  <div class="btn-line" style="left:323px;top:1491px;width:78px;height:19px;background:#fff">VIEW ALL FORUM</div>

  <!-- Photo feed -->
  <div class="rule" style="left:250px;top:1606px;width:45px"></div>
  <svg style="position:absolute;left:307px;top:1598px" width="14" height="14" viewBox="0 0 14 14"><rect x="0" y="0" width="14" height="14" rx="2" fill="var(--blue)"/></svg>
  <h2 class="sec-title" style="left:333px;top:1594px">Instagram</h2>
  <div class="rule" style="left:429px;top:1606px;width:46px"></div>
  <div style="left:0;top:1620px;width:724px;text-align:center;font-size:6.5px;color:var(--red);letter-spacing:.3px">Follow@builtonthegrind</div>
  <div class="img" role="img" aria-label="Friends high-fiving at the gym" style="left:0;top:1646px;width:145px;height:107px;background:linear-gradient(120deg,#4a3f38,#a3846c)"></div>
  <div class="img" role="img" aria-label="Meal planning with healthy food" style="left:145px;top:1646px;width:145px;height:107px;background:linear-gradient(120deg,#d7cfc4,#a98f7a)"></div>
  <div class="img" role="img" aria-label="Healthy food and skipping rope with blue overlay" style="left:290px;top:1646px;width:145px;height:107px;background:linear-gradient(120deg,#2d5a8e,#3f75a8)"></div>
  <div class="img" role="img" aria-label="Woman exercising at home with a laptop" style="left:435px;top:1646px;width:145px;height:107px;background:linear-gradient(120deg,#6a6e6a,#a7a39b)"></div>
  <div class="img" role="img" aria-label="Woman lifting dumbbells" style="left:580px;top:1646px;width:144px;height:107px;background:linear-gradient(120deg,#8a7e78,#3a3333)"></div>

  <!-- Footer -->
  <footer style="left:0;top:1753px;width:724px;height:132px;background:var(--band)"></footer>
  <div class="brand" style="left:45px;top:1810px;font-size:12px"><i></i>Built on the grind</div>
  <div class="foot-nav" style="left:198px;top:1793px;color:var(--red)">Home</div>
  <div class="foot-nav" style="left:237px;top:1793px">About Us</div>
  <div class="foot-nav" style="left:288px;top:1793px">Nutrition</div>
  <div class="foot-nav" style="left:340px;top:1793px">Training</div>
  <div class="foot-nav" style="left:389px;top:1793px">Workouts</div>
  <div class="foot-nav" style="left:443px;top:1793px">Forum</div>
  <div class="foot-nav" style="left:484px;top:1793px">Contact Us</div>
  <div class="rule" style="left:185px;top:1830px;width:355px;background:#b8c3d3"></div>
  <div class="dot" style="left:327px;top:1822px;width:17px;height:17px;border:3px solid var(--band)"></div>
  <div class="dot" style="left:353px;top:1822px;width:17px;height:17px;border:3px solid var(--band);background:var(--blue)"></div>
  <div class="dot" style="left:379px;top:1822px;width:17px;height:17px;border:3px solid var(--band)"></div>
  <div style="left:0;top:1858px;width:724px;text-align:center;font-size:6.3px">© 2022 <span style="position:static;color:var(--blue)">Built on the grind</span>. All Right Reserved.</div>
  <svg style="position:absolute;left:668px;top:1810px" width="20" height="20" viewBox="0 0 20 20"><rect x="4" y="4" width="12" height="12" transform="rotate(45 10 10)" fill="var(--red)"/><path d="M7 11.5 L10 8.5 L13 11.5" stroke="#fff" stroke-width="1.4" fill="none"/></svg>
</main>
</body>
</html>
```